Nutrition-Cooking Website

Hello!
I am in a need of a lovely looking website for my new nutrition practice. I am looking for something sleek, sophisticated, professional yet also welcoming.

Here is a current layout which can be tweaked or overhauled. I feel like the website is not quite what I want so thats why I need your help!!
http://tolvanfolio.example/RENATA-OSSLER-concept-15/

Two websites I like are: (layout similar to www.marquetta.example) or http://www.pernillavostraken.example

Here are the tabs for the website:
About Registered Dietitian Healthy Recipes Philanthropy Shop Features Contact Blog

Features for the Home page include:
Slideshow with 3 rotating updates (like www.marquetta.example)
Video Box (like www.marquetta.example)
Recent Recipes (like http://harrowfield7731.example)
Recent Posts (like http://harrowfield7731.example)
Food Knowledge Box- quick tidbits on laws on food (like www.marquetta.example- she has food wisdom)
Tried and True Benefits of Mediterranean Cuisine (like www.marquetta.example)
Picture of me with brief quote/bio (like www.bettinoruval.example)
Social media buttons

Color Scheme:
• I like the white with gold embroidery or the pretty bluish/purplish in the first pic would be awesome with the slight pink undertones (http://glossedtwirl.example/2012/10/quorvel-marigelle-collection-by-tansley/)
• Also like this goldish background- exotic/sophisticated- http://www.thewhirlingcook.example/Home.html
• Also like the rustic goldish look in the background like this-
ohttp://img.prentlo.example/vexomarks_rsvp_vintage_rustic_gold_swirls_invitation-p161658028764768924bebn6_400.jpg
o http://img.prentlo.example/vexomarks_ornamental_rustic_gold_swirls_invitation-p161776340110432961bvddb_400.jpg
• maybe can have the vines as grapes/olives
OPEN TO ALL DIFFERENT COLORS SCHEMES- whatever looks, clean, sophisticated and professional

Logo:
• Attached is the logo

Budget is flexible. If you think you can improve the website- please do so :)

Target Market(s)

health conscious individuals of all ages

Industry/Entity Type

Embroidery

Requirements
Must have
• clean and sharp look
professional looking
Should not have
• too much busyness

```html
<!DOCTYPE html>
<html lang="en">
<head>
<meta charset="utf-8">
<title>Renata Ossler RD – Nutrition &amp; Cooking</title>
<link rel="stylesheet" href="https://fonts.googleapis.com/css2?family=Cinzel:wght@400;600&family=Dancing+Script:wght@400;600&family=Handlee&display=swap">
<style>
:root{
  --bg-dark:#3b2a14;
  --bg-mid:#5a4322;
  --page:#ffffff;
  --gold:#c9a24a;
  --gold-light:#f2dc93;
  --gold-deep:#8a6418;
  --brown:#5b3c12;
  --brown-text:#6b4a1c;
  --olive:#4a6a12;
  --green:#8cc21f;
  --green-dark:#5f9410;
  --grey:#7a7a7a;
  --line:#e3dccb;
  --footer:#f1df9d;
  --footer-light:#f7eabb;
  --login:#c4121b;
  --sky:#2f9bd6;
}
*{box-sizing:border-box;margin:0;padding:0}
html,body{width:723px;height:1200px;overflow:hidden}
body{background:linear-gradient(90deg,var(--bg-dark) 0,var(--bg-mid) 10%,var(--bg-mid) 90%,var(--bg-dark) 100%);font-family:Arial,Helvetica,sans-serif;color:var(--grey);position:relative}
.abs{position:absolute}
.nowrap{white-space:nowrap}
.page{position:absolute;left:72px;top:0;width:579px;height:1200px;background:var(--page)}
.site-footer{position:absolute;left:72px;top:1010px;width:579px;height:190px;background:linear-gradient(180deg,var(--footer) 0,var(--footer-light) 100%)}
.social{display:flex;gap:4px}
.social span{width:14px;height:14px;border:1.5px solid var(--gold);border-radius:50%;display:block}
.phone{font-family:'Cinzel',serif;font-size:10px;color:var(--brown-text);display:flex;align-items:center;gap:4px;white-space:nowrap}
.brand{font-family:'Cinzel',serif;font-weight:400;font-size:17px;letter-spacing:1px;color:var(--brown);text-align:center;white-space:nowrap}
.search{border:1px solid #d8d8d8;border-radius:9px;width:78px;height:15px;font-size:7px;color:#aaa;padding:3px 8px;text-transform:uppercase}
.login{background:var(--login);color:#fff;font-size:8px;border-radius:8px;padding:3px 8px;font-family:'Cinzel',serif;font-weight:600}
.main-nav{left:66px;top:64px;width:592px;height:31px;background:linear-gradient(180deg,#b9913b 0,#8e6a1f 55%,#6e4f12 100%);display:flex;align-items:center;justify-content:center;gap:3px;box-shadow:0 2px 3px rgba(0,0,0,.35)}
.main-nav a{font-family:'Cinzel',serif;font-size:9px;color:#fff;text-decoration:none;padding:3px 6px;white-space:nowrap;text-transform:uppercase}
.main-nav a.active{background:linear-gradient(180deg,#fff6cf,#e8c66c);color:var(--brown);border-radius:10px;padding:3px 9px}
.hero-quote{font-family:'Handlee',cursive;font-size:23px;line-height:27px;color:var(--brown-text)}
.hero-sub{font-family:'Cinzel',serif;font-size:11px;line-height:14px;color:#8d857a;letter-spacing:.3px}
.btn-green{background:linear-gradient(180deg,var(--green),var(--green-dark));color:#fff;font-family:'Cinzel',serif;font-size:10px;border-radius:14px;padding:8px 13px;letter-spacing:.5px;white-space:nowrap}
.hero-note{font-family:'Dancing Script',cursive;font-size:9.5px;color:var(--olive);white-space:nowrap}
.arrow-round{width:24px;height:24px;border-radius:50%;background:rgba(255,255,255,.15);display:flex;align-items:center;justify-content:center}
.welcome{font-family:'Cinzel',serif;font-size:6.4px;line-height:11px;color:var(--olive);text-align:center;white-space:nowrap}
.welcome b{color:#2f7a12;font-weight:600}
.btn-gold{background:linear-gradient(180deg,var(--gold-light),var(--gold));color:var(--brown);font-family:'Cinzel',serif;font-size:6.5px;border-radius:8px;padding:4px 10px;white-space:nowrap}
.col-title{font-family:'Dancing Script',cursive;font-weight:400;font-size:15px;color:var(--brown-text);text-align:center;width:168px;white-space:nowrap}
.col-rule{height:1px;background:var(--line);width:150px}
.divider-v{width:1px;background:var(--line)}
.photo{border-radius:2px}
.post-title{font-family:'Cinzel',serif;font-weight:400;font-size:8.5px;line-height:10px;color:var(--gold-deep);white-space:nowrap}
.post-text{font-size:7px;line-height:9.5px;color:var(--grey)}
.date{width:22px;height:22px;border:1.5px solid var(--gold-deep);border-radius:50%;background:#fff;font-family:'Cinzel',serif;font-size:6.5px;line-height:7px;color:var(--brown);text-align:center;padding-top:3px}
.tile-label{font-family:'Dancing Script',cursive;font-size:15px;color:#fff;white-space:nowrap}
.tweets-title{font-family:'Dancing Script',cursive;font-size:15px;color:var(--sky);text-align:center}
.tweet{font-size:7.3px;color:var(--grey);text-align:center;width:579px;white-space:nowrap}
.foot-title{font-family:'Cinzel',serif;font-weight:400;font-size:10.5px;color:var(--brown);white-space:nowrap}
.foot-links{font-size:8px;line-height:13.5px;color:#4d3a1a;list-style:none}
.foot-links li:first-child{text-decoration:underline}
.email{background:#fff;border:1px solid #d8c07a;border-radius:8px;width:108px;height:14px;font-size:7px;color:#aaa;padding:2px 7px}
.signup{background:linear-gradient(180deg,#8a6a2a,#5d4215);color:#fff;font-family:'Cinzel',serif;font-size:7px;border-radius:8px;padding:3px 10px;white-space:nowrap}
.fine{font-size:6px;color:#5a4a2a;text-align:center;width:579px}
</style>
</head>
<body>
<div class="page"></div>

<header>
  <div class="abs social" style="left:88px;top:29px"><span></span><span></span><span></span></div>
  <div class="abs phone" style="left:143px;top:30px">
    <svg width="14" height="14" viewBox="0 0 14 14"><circle cx="7" cy="7" r="6.2" fill="none" stroke="#c9a24a" stroke-width="1.3"/><path d="M4.6 3.8l1.4 1.6-.7.9a5 5 0 0 0 2.5 2.5l.9-.7 1.6 1.4-.9 1.1C7.1 10.4 3.7 7 3.6 4.7z" fill="#c9a24a"/></svg>
    0400 5512 7788
  </div>
  <div class="abs brand" style="left:240px;top:25px;width:243px">RENATA OSSLER RD</div>
  <div class="abs search" style="left:532px;top:29px">Search</div>
  <div class="abs login" style="left:618px;top:29px">LOGIN</div>
</header>

<nav class="abs main-nav">
  <a href="#">About</a><a href="#">Registered</a><a href="#">Dietitian</a><a href="#" class="active">Healthy Recipes</a><a href="#">Philanthropy</a><a href="#">Shop</a><a href="#">Features</a><a href="#">Contact</a><a href="#">Blog</a>
</nav>

<section class="hero">
  <div class="abs" role="img" aria-label="Fresh fruit and vegetables arranged across the foot of the banner" style="left:72px;top:240px;width:455px;height:99px;background:linear-gradient(180deg,rgba(255,255,255,0) 0,#c7d98a 35%,#b8472f 70%,#8fb33a 100%)"></div>
  <div class="abs" role="img" aria-label="Smiling woman lifting a blue dumbbell" style="left:527px;top:95px;width:124px;height:244px;background:linear-gradient(180deg,#f3efe7 0,#c79a78 45%,#efe9e2 100%)"></div>
  <p class="abs hero-quote" style="left:108px;top:124px;width:360px">One cannot think well, love well.<br>If one has not dined well</p>
  <p class="abs hero-sub" style="left:109px;top:189px;width:360px">CONSECTETUR ADIPISICING ELIT, SED DO EIUSMOD TEMPOR INCIDIDUNT UT LABORE ET DOLORE MAGNA ALIQUA.</p>
  <div class="abs btn-green" style="left:121px;top:245px">SEE HEALTHY NUTRITION</div>
  <div class="abs hero-note" style="left:132px;top:272px">Registration free for Cooking Class</div>
  <div class="abs arrow-round" style="left:40px;top:200px"><svg width="10" height="10" viewBox="0 0 10 10"><path d="M6.5 1.5L3 5l3.5 3.5" fill="none" stroke="#cbbda0" stroke-width="1.6"/></svg></div>
  <div class="abs arrow-round" style="left:659px;top:200px"><svg width="10" height="10" viewBox="0 0 10 10"><path d="M3.5 1.5L7 5 3.5 8.5" fill="none" stroke="#cbbda0" stroke-width="1.6"/></svg></div>
</section>

<svg class="abs" style="left:342px;top:351px" width="38" height="14" viewBox="0 0 38 14"><circle cx="6" cy="7" r="3.5" fill="none" stroke="#8a6418" stroke-width="1.2"/><circle cx="19" cy="7" r="5.5" fill="none" stroke="#8a6418" stroke-width="1.4"/><circle cx="32" cy="7" r="3.5" fill="none" stroke="#8a6418" stroke-width="1.2"/></svg>

<p class="abs welcome" style="left:72px;top:373px;width:579px"><b>WELCOME TO RENATA OSSLER</b> ENIM AD MINIM VENIAM, QUIS NOSTRUD EXERCITATION ULLAMCO LABORIS NISI UT ALIQUIP EX EA COMMODO<br>CONSEQUAT. DUIS AUTE IRURE DOLOR IN REPREHENDERIT IN VOLUPTATE VELIT ESSE CILLUM DOLORE EU FUGIAT NULLA PARIATUR</p>
<div class="abs btn-gold" style="left:333px;top:404px">LEARN MORE</div>

<div class="abs divider-v" style="left:266px;top:442px;height:440px"></div>
<div class="abs divider-v" style="left:457px;top:442px;height:440px"></div>

<section class="recent-posts">
  <h2 class="abs col-title" style="left:88px;top:443px">Recent Post</h2>
  <div class="abs col-rule" style="left:91px;top:479px"></div>
  <article>
    <div class="abs photo" role="img" aria-label="Pomegranate chocolate cupcakes" style="left:91px;top:501px;width:64px;height:45px;background:linear-gradient(135deg,#e6d9d0,#a8241c)"></div>
    <h3 class="abs post-title" style="left:163px;top:503px">Pomegranate<br>Chocolate Cupcakes.</h3>
    <p class="abs post-text" style="left:163px;top:526px;width:90px">Ut enim ad minim veniam, quis nostrud exercitationUt enim ad minim veniam</p>
    <div class="abs date" style="left:158px;top:557px">22<br>FEB</div>
  </article>
  <article>
    <div class="abs photo" role="img" aria-label="Chocolate cake slice" style="left:91px;top:596px;width:64px;height:45px;background:linear-gradient(135deg,#5a3a2c,#2b1b14)"></div>
    <h3 class="abs post-title" style="left:163px;top:597px">Pomegranate<br>Chocolate Cupcakes.</h3>
    <p class="abs post-text" style="left:163px;top:620px;width:90px">Ut enim ad minim veniam, quis nostrud exercitationUt enim ad minim veniam</p>
    <div class="abs date" style="left:158px;top:651px">21<br>FEB</div>
  </article>
  <article>
    <div class="abs photo" role="img" aria-label="Chocolate mousse dessert" style="left:91px;top:695px;width:64px;height:45px;background:linear-gradient(135deg,#e2c7ae,#9a6a4a)"></div>
    <h3 class="abs post-title" style="left:163px;top:696px">Pomegranate<br>Chocolate Cupcakes.</h3>
    <p class="abs post-text" style="left:163px;top:719px;width:90px">Ut enim ad minim veniam, quis nostrud exercitationUt enim ad minim veniam</p>
    <div class="abs date" style="left:158px;top:750px">20<br>FEB</div>
  </article>
  <article>
    <div class="abs photo" role="img" aria-label="Berry dessert with cream" style="left:91px;top:792px;width:64px;height:45px;background:linear-gradient(135deg,#cfd0d8,#6a2a3a)"></div>
    <h3 class="abs post-title" style="left:163px;top:794px">Pomegranate<br>Chocolate Cupcakes.</h3>
    <p class="abs post-text" style="left:163px;top:817px;width:90px">Ut enim ad minim veniam, quis nostrud exercitationUt enim ad minim veniam</p>
    <div class="abs date" style="left:158px;top:848px">19<br>FEB</div>
  </article>
</section>

<section class="recent-recipes">
  <h2 class="abs col-title" style="left:277px;top:443px">Recent Recipes</h2>
  <div class="abs col-rule" style="left:286px;top:479px"></div>
  <div class="abs photo" role="img" aria-label="Pancakes topped with pomegranate seeds" style="left:277px;top:504px;width:169px;height:80px;background:linear-gradient(135deg,#4a5060,#b07a4a 50%,#7a1a22)"></div>
  <h3 class="abs post-title" style="left:277px;top:592px">Pomegranate Chocolate Cupcakes<br>with Buttercream Frosting</h3>
  <p class="abs post-text" style="left:277px;top:614px;width:169px">Lorem enim ad minim veniam, quis nostrud...</p>
  <div class="abs photo" role="img" aria-label="Halved pomegranates" style="left:277px;top:638px;width:169px;height:80px;background:linear-gradient(135deg,#b01a20,#5a0a10 60%,#d8cfc8)"></div>
  <h3 class="abs post-title" style="left:277px;top:726px">Pomegranate Chocolate Cupcakes.</h3>
  <p class="abs post-text" style="left:277px;top:739px;width:169px">Lorem enim ad minim veniam, quis nostrud...</p>
  <div class="abs photo" role="img" aria-label="Chocolate-dipped pomegranate seeds" style="left:277px;top:764px;width:169px;height:80px;background:linear-gradient(135deg,#3a1e16,#a81a1e 55%,#4a2a1e)"></div>
  <h3 class="abs post-title" style="left:277px;top:852px">Lorem Eiusmod Tempor Incididunt</h3>
  <p class="abs post-text" style="left:277px;top:865px;width:169px">Lorem enim ad minim veniam, quis nostrud...</p>
</section>

<section class="video-box">
  <h2 class="abs col-title" style="left:467px;top:443px">Renata Ossler RD Video</h2>
  <div class="abs col-rule" style="left:476px;top:479px"></div>
  <div class="abs photo" role="img" aria-label="Video still of a kitchen scene" style="left:467px;top:504px;width:168px;height:108px;background:linear-gradient(135deg,#3a2a22,#8a6a52 55%,#2a1e18);box-shadow:0 3px 4px rgba(0,0,0,.3)"></div>
  <svg class="abs" style="left:537px;top:544px" width="28" height="28" viewBox="0 0 28 28"><circle cx="14" cy="14" r="12.5" fill="none" stroke="#fff" stroke-width="1.5"/><path d="M11 8.5l8 5.5-8 5.5z" fill="#fff"/></svg>
  <p class="abs" style="left:467px;top:578px;width:168px;text-align:center;font-family:'Cinzel',serif;font-size:7px;color:#fff">RENATA OSSLER RD VIDEO</p>
  <div class="abs photo" role="img" aria-label="Apple with measuring tape" style="left:467px;top:637px;width:168px;height:76px;background:linear-gradient(135deg,#3a3a3a,#7a8a3a 45%,#4a4a4a)"></div>
  <p class="abs tile-label" style="left:505px;top:668px">Food Philosophy</p>
  <p class="abs post-text" style="left:467px;top:721px;width:168px">Lorem enim ad minim veniam, quis nostrud exercitationUt enim ad minim veniam</p>
  <div class="abs photo" role="img" aria-label="Fresh salad in a bowl" style="left:467px;top:757px;width:168px;height:76px;background:linear-gradient(135deg,#3a3a3a,#a84a3a 45%,#5a6a3a)"></div>
  <p class="abs tile-label" style="left:505px;top:789px">Food knowledge</p>
  <p class="abs post-text" style="left:467px;top:841px;width:168px">Lorem enim ad minim veniam, quis nostrud exercitationUt enim ad minim veniam</p>
</section>

<section class="tweets">
  <h2 class="abs tweets-title" style="left:72px;top:893px;width:579px">See Our Chirper Tweets</h2>
  <div class="abs" style="left:290px;top:921px;width:144px;height:1px;background:linear-gradient(90deg,transparent,#bcdcee,transparent)"></div>
  <svg class="abs" style="left:357px;top:916px" width="10" height="10"><circle cx="5" cy="5" r="4" fill="#2f9bd6"/></svg>
  <p class="abs tweet" style="left:72px;top:932px">Ut enim ad minim veniam, quis nostrud exercitationUt enim ad minim veniamUt enim ad minim veniam, quis nostrud exercitationUt enim veniam</p>
  <p class="abs tweet" style="left:72px;top:944px;color:#333">http://lnk.example/DKYohjwF &nbsp;about 2 hour ago</p>
  <svg class="abs" style="left:349px;top:963px" width="26" height="12" viewBox="0 0 26 12"><circle cx="6" cy="6" r="5" fill="none" stroke="#777"/><path d="M7 3.5L4.5 6 7 8.5" fill="none" stroke="#555"/><circle cx="20" cy="6" r="5" fill="none" stroke="#777"/><path d="M19 3.5L21.5 6 19 8.5" fill="none" stroke="#555"/></svg>
</section>

<footer>
  <div class="site-footer"></div>
  <div class="abs" role="img" aria-label="Portrait of the dietitian holding a dumbbell beside a fruit bowl" style="left:110px;top:961px;width:92px;height:56px;background:linear-gradient(180deg,#f1ece4 0,#c79a78 45%,#8fb33a 100%);border-radius:40px 40px 0 0"></div>

  <h2 class="abs foot-title" style="left:97px;top:1040px">Browse Company</h2>
  <ul class="abs foot-links" style="left:97px;top:1063px"><li>About</li><li>Registered</li><li>Dietitian</li><li>Healthy Recipes</li><li>Philanthropy</li></ul>
  <ul class="abs foot-links" style="left:179px;top:1063px;line-height:18px"><li style="text-decoration:none">Shop</li><li>Features</li><li>Contact</li><li>Blog</li></ul>

  <h2 class="abs foot-title" style="left:247px;top:1040px">Renata's Blog Post</h2>
  <div class="abs photo" role="img" aria-label="Berry dessert with cream" style="left:248px;top:1065px;width:65px;height:43px;background:linear-gradient(135deg,#d8d4d8,#6a2a3a)"></div>
  <h3 class="abs post-title" style="left:321px;top:1066px;color:var(--brown)">Pomegranate Chocolate<br>Cupcakes.</h3>
  <p class="abs post-text" style="left:321px;top:1089px;width:132px;color:#4d3a1a">Ut enim ad minim veniam, quis nostrud exercitationUt enim ad minim veniam</p>
  <p class="abs post-text nowrap" style="left:321px;top:1111px;color:#4d3a1a">19,Feb 2013 &nbsp;<u>Read More</u></p>

  <h2 class="abs foot-title" style="left:479px;top:1040px">Join Renata's Newsletter</h2>
  <div class="abs email" style="left:477px;top:1063px">Enter Email</div>
  <div class="abs signup" style="left:477px;top:1083px">SIGNUP FREE</div>
  <div class="abs social" style="left:479px;top:1107px"><span></span><span></span><span></span></div>
  <div class="abs phone" style="left:533px;top:1107px">
    <svg width="14" height="14" viewBox="0 0 14 14"><circle cx="7" cy="7" r="6.2" fill="none" stroke="#c9a24a" stroke-width="1.3"/><path d="M4.6 3.8l1.4 1.6-.7.9a5 5 0 0 0 2.5 2.5l.9-.7 1.6 1.4-.9 1.1C7.1 10.4 3.7 7 3.6 4.7z" fill="#c9a24a"/></svg>
    0400 5512 7788
  </div>

  <div class="abs" style="left:97px;top:1147px;width:530px;height:1px;background:#dcc77f"></div>
  <p class="abs fine" style="left:72px;top:1156px">All Right Reserved Copyright © 2013 &nbsp;- &nbsp;Privacy Policy &nbsp;- &nbsp;Terms of use</p>
  <p class="abs fine" style="left:72px;top:1167px">Powered by Brightleaf Studio</p>
</footer>
</body>
</html>
```